Lotus Ember menu projecting our true authentic nature

We need a take out menu that is inviting and expresses the authentic nature of our Thai food. Also something that expresses the Thai culture. We have attached a current menu that is in need of updating. This take out menu should be something that says to potential customers "this is where I need to go." While we are Asian in nature we are specifically Thai and need to have a project that projects the Thai culture not simply Asian.

Target Market(s)

Locals and interstate traveers, college nearby, hospital personnel, mid 20s to 60s.

Industry/Entity Type

Asian Restaurant

Colors

Designer to choose colors to be used in the design.

Requirements
Must have
• Elegant, attractive features that enhance the Thai culture and provides a bit of an upscale look and appeal but that also says not overpriced for the more economical.

```html
<!DOCTYPE html>
<html lang="en">
<head>
<meta charset="utf-8">
<title>Lotus Ember Take Out Menu</title>
<link href="https://fonts.googleapis.com/css2?family=Cinzel:wght@400;600&family=Josefin+Sans:ital,wght@0,300;0,400;1,300;1,400&display=swap" rel="stylesheet">
<style>
:root{
  --plum:#5a2a6c;
  --plum-deep:#4a1f5c;
  --plum-soft:#6a3a7e;
  --ink:#2a2230;
  --paper:#ffffff;
  --paper-grey:#f3f2f4;
}
*{margin:0;padding:0;box-sizing:border-box}
html,body{width:1200px;height:894px;overflow:hidden;background:var(--paper)}
body{position:relative;font-family:"Josefin Sans",sans-serif;color:var(--ink)}
.panel{position:absolute;border-radius:3px}
.panel--plum{background:linear-gradient(160deg,var(--plum-soft),var(--plum) 45%,var(--plum-deep));color:#fff}
.panel--grey{background:var(--paper-grey)}
.section{position:absolute}
.ornament{position:absolute;left:50%;transform:translateX(-50%);border-radius:4px}
.ornament--light{background:linear-gradient(#f3eef6,#d9cde0);opacity:.85}
.ornament--dark{background:linear-gradient(#555,#222);opacity:.8}
.heading{font-family:"Cinzel",serif;font-weight:400;text-align:center;letter-spacing:.5px;line-height:1}
.sub{font-family:"Cinzel",serif;font-size:7.6px;text-align:center;line-height:1.15;letter-spacing:.3px;font-variant:small-caps}
.menu{list-style:none;position:relative;z-index:2}
.item{display:grid;grid-template-columns:22px 1fr;margin-bottom:2px}
.menu--wide .item{grid-template-columns:30px 1fr}
.num{font-size:11px;line-height:12px}
.name{font-size:11.6px;line-height:12px;text-transform:uppercase;font-weight:300;letter-spacing:.1px}
.price{font-size:8px;text-transform:none;margin-left:2px}
.desc{display:block;font-style:italic;font-weight:300;font-size:9.6px;line-height:10.4px;text-transform:none}
.photo{position:absolute;border-radius:50%;z-index:1}
.indent{padding-left:12px}
.kids{position:absolute;left:410px;top:768px;width:380px;text-align:center;text-transform:uppercase}
.kids h2{font-weight:300;font-size:21px;letter-spacing:1px;line-height:24px}
.kids p{font-size:8.6px;line-height:9.6px}
.kids h3{font-weight:300;font-size:12px;margin-top:4px;line-height:14px}
</style>
</head>
<body>

<section class="panel panel--plum" style="left:10px;top:8px;width:380px;height:574px">
  <div class="ornament ornament--light" role="img" aria-label="Thai temple guardian ornament" style="top:16px;width:28px;height:56px"></div>
  <h1 class="heading" style="position:absolute;top:74px;width:100%;font-size:24px">Appetizers</h1>
  <ol class="menu" style="position:absolute;left:34px;top:104px;width:320px">
    <li class="item"><span class="num">1.</span><span class="name">Fried Spring Rolls <span class="price">(2) 1.79 (4) 3.59 (6) 4.49 (12) 8.99</span><span class="desc">Rice wrapper filled with cabbage, carrot and bean thread<br>noodles rolled &amp; deep-fried</span></span></li>
    <li class="item"><span class="num">2.</span><span class="name">Fresh Spring Rolls <span class="price">(2) 5.49</span><span class="desc">Soft rice wrapper filled with an array of shrimp, beef &amp; fresh<br>vegetables served with Pineapple or Peanut Sauce<br>(Both add 99¢)</span></span></li>
    <li class="item"><span class="num">3.</span><span class="name">Fried Cheese Wontons <span class="price">(6) 3.49 (12) 5.89</span><span class="desc">Thin pastry stuffed with seasoned cream cheese mixture<br>&amp; deep-fried</span></span></li>
    <li class="item indent"><span class="num">3.A</span><span class="name">&nbsp;Fried Wontons Variety Pack <span class="price">(12) 6.39</span><span class="desc">6 Fried Cheese Wontons &amp; 6 Fried Chicken Wontons</span></span></li>
    <li class="item"><span class="num">4.</span><span class="name">Fried Chicken Wontons <span class="price">(6) 4.29 (12) 6.79</span><span class="desc">Thin pastry stuffed with a thin layer of seasoned ground chicken<br>&amp; fried to a golden crisp</span></span></li>
    <li class="item"><span class="num">5.</span><span class="name">Spicy Meatballs <span class="price">(6) 3.99 (12) 6.79</span><span class="desc">Seasoned meatballs tossed<br>in our sweet &amp; spicy house<br>sauce</span></span></li>
    <li class="item"><span class="num">6.</span><span class="name">Tofu Todd <span class="price">4.99</span><span class="desc">Crispy fried tofu served with<br>our House Sweet &amp; Spicy<br>Sauce &amp; ground peanuts</span></span></li>
    <li class="item"><span class="num">7.</span><span class="name">Satay Kai (Chicken Satay) <span class="price">6.99</span><span class="desc">Succulent skewered strips of<br>marinated chicken breast pan seared, served with our<br>homemade peanut sauce &amp; cucumber sauce</span></span></li>
    <li class="item"><span class="num">8.</span><span class="name">Shrimp Rolls <span class="price">(3) 4.99 (6) 9.79</span><span class="desc">Jumbo shrimp lightly seasoned, wrapped in a thin pastry<br>then deep-fried to perfection</span></span></li>
    <li class="item"><span class="num">9.</span><span class="name">Thai Style Chicken Wings <span class="price">(5) 4.79 (10) 8.99 (20) 16.49</span><span class="desc">Our special marinated chicken wings are deep fried until<br>golden &amp; crisp then tossed in our sweet &amp; spicy house sauce.</span></span></li>
    <li class="item"><span class="num"></span><span class="name">Fried Chicken Wings <span class="price">(5) 4.79 (10) 8.99 (20) 16.49</span></span></li>
    <li class="item"><span class="num"></span><span class="name">Thai Sampler <span class="price">11.99</span><span class="desc">Fried Spring Rolls, Cheese Wontons, Spicy Meatballs, &amp; Wings</span></span></li>
  </ol>
  <div class="photo" role="img" aria-label="Photo of fried spring rolls with sweet chili dipping sauce on a white plate" style="left:212px;top:280px;width:152px;height:96px;background:radial-gradient(circle at 30% 50%,#b3341e 0 18%,#f1e5cf 19% 40%,#d79a4a 41% 55%,#f6f3ee 56%)"></div>
</section>

<section class="panel panel--grey" style="left:10px;top:592px;width:380px;height:292px">
  <div class="ornament ornament--dark" role="img" aria-label="Thai temple guardian ornament" style="top:6px;width:26px;height:52px"></div>
  <h2 class="heading" style="position:absolute;top:62px;width:100%;font-size:22px">Fried Rice</h2>
  <p class="sub" style="position:absolute;top:86px;width:100%">Steamed rice stir fried with our special Thai sauce, carrots, &amp; onions<br>Add Pineapple 99¢ Add Fried Spring Rolls (2) 1.79 (4) 3.59</p>
  <ol class="menu" style="position:absolute;left:34px;top:112px;width:330px">
    <li class="item" style="grid-template-columns:36px 1fr"><span class="num">10A.</span><span class="name">Beef Fried Rice* <span class="price">8.99 Thai Style 9.99</span></span></li>
    <li class="item" style="grid-template-columns:36px 1fr"><span class="num">10B.</span><span class="name">Chicken, Roast Pork, or Pork <span class="price">7.99 Thai Style 8.99</span></span></li>
    <li class="item" style="grid-template-columns:36px 1fr"><span class="num">10C.</span><span class="name">Vegetarian (Tofu on request) <span class="price">Thai Style 8.99</span></span></li>
    <li class="item" style="grid-template-columns:36px 1fr"><span class="num">10D.</span><span class="name">Pineapple Fried Rice <span class="price">9.29 Thai Style 10.29</span><span class="desc">Steamed rice stir-fried with special Thai sauce, chicken,<br>chunks of pineapple, raisins, cashew, carrots, &amp; onions</span></span></li>
    <li class="item" style="grid-template-columns:36px 1fr"><span class="num">10E.</span><span class="name">Shrimp Pineapple Fried Rice <span class="price">9.99 Thai Style 10.99</span><span class="desc">Steamed rice stir-fried with special Thai sauce, chicken,<br>chunks of pineapple, raisins, cashew, carrots, &amp; onions</span></span></li>
    <li class="item" style="grid-template-columns:36px 1fr"><span class="num">11.</span><span class="name">Shrimp Fried Rice <span class="price">8.69 Thai Style 9.69</span></span></li>
    <li class="item" style="grid-template-columns:36px 1fr"><span class="num">12.</span><span class="name">House Fried Rice <span class="price">(3) 4.99 (6) 9.79</span><span class="desc">Steamed rice stir-fried with chicken, beef, shrimp,<br>our special Thai sauce, carrots, &amp; onions</span></span></li>
  </ol>
</section>

<section class="section" style="left:410px;top:24px;width:380px;height:384px">
  <div class="ornament ornament--dark" role="img" aria-label="Illustration of a seated Thai dancer" style="top:8px;width:40px;height:52px"></div>
  <h2 class="heading" style="position:absolute;top:62px;width:100%;font-size:24px">Soups</h2>
  <ol class="menu" style="position:absolute;left:30px;top:88px;width:340px">
    <li class="item"><span class="num">13.</span><span class="name">Kangjuedwoonsen <span class="price">8.49</span><span class="desc">Ground pork, glass noodles, Napa cabbage,<br>mushrooms, &amp; green onions in a clear<br>broth, topped with cilantro</span></span></li>
    <li class="item"><span class="num">14.</span><span class="name">Tom Yum Koong <span class="price">10.99</span><span class="desc">Lemongrass soup with hot/sour shrimp, mushrooms,<br>tomatoes &amp; lemon juice</span></span></li>
    <li class="item"><span class="num">15.</span><span class="name">Tom Yum Gai <span class="price">8.49</span><span class="desc">Lemongrass soup with hot/<br>sour chicken, mushrooms,<br>tomatoes, &amp; Lemon juice</span></span></li>
    <li class="item"><span class="num">16.</span><span class="name">Tom Kha Gai <span class="price">9.99</span><span class="desc">Lemongrass soup with hot/sour<br>chicken, mushrooms,<br>tomatoes, coconut milk, galangal,<br>&amp; Lemon juice</span></span></li>
    <li class="item"><span class="num">17.</span><span class="name">Tom Kha Koong <span class="price">11.99</span><span class="desc">Lemongrass soup with hot/sour shrimp, mushrooms,<br>tomatoes, coconut milk, galangal, &amp; Lemon juice</span></span></li>
    <li class="item"><span class="num">18.</span><span class="name">Khao Tom (Rice Soup) <span class="price">Chicken 8.49 Shrimp 11.49</span><span class="desc">Steamed rice with choice of meat, fresh celery,<br>garlic &amp; cilantro</span></span></li>
    <li class="item"><span class="num">19.</span><span class="name">Tofu Soup <span class="price">Chicken 8.49 Shrimp 11.49</span><span class="desc">Tofu, cilantro, bean thread noodles, &amp; Chinese cabbage</span></span></li>
  </ol>
  <div class="photo" role="img" aria-label="Photo of tom yum soup with shrimp and mushrooms in a white bowl" style="left:248px;top:170px;width:110px;height:100px;background:radial-gradient(circle,#d98a3c 0 40%,#e9b56a 55%,#f4f0ea 62%,#fff 72%)"></div>
</section>

<section class="panel panel--plum" style="left:410px;top:422px;width:380px;height:294px">
  <div class="ornament ornament--light" role="img" aria-label="Illustration of a seated Thai dancer" style="top:10px;width:40px;height:58px"></div>
  <h2 class="heading" style="position:absolute;top:68px;width:100%;font-size:22px">Thai Salads</h2>
  <p class="sub" style="position:absolute;top:90px;width:100%">All salads tossed in our special spicy,<br>lemony dressing &amp; steam rice</p>
  <ol class="menu" style="position:absolute;left:28px;top:112px;width:340px">
    <li class="item"><span class="num">20.</span><span class="name">Yum Nuer <span class="price">9.49</span><span class="desc">Sliced BBQ beef, with lettuce, cucumbers, &amp; red onions</span></span></li>
    <li class="item"><span class="num">21.</span><span class="name">Yum Pla Muk <span class="price">12.49</span><span class="desc">Fresh cooked squid, mixed in a blend of lemongrass, red<br>onions, &amp; Lotus Ember paste served on a bed of lettuce</span></span></li>
    <li class="item"><span class="num">23.</span><span class="name">Pla Koong <span class="price">12.49</span><span class="desc">Large shrimp mixed in a<br>blend of lemon-grass, red<br>onions &amp; Lotus Ember paste<br>served on a bed of lettuce</span></span></li>
    <li class="item"><span class="num">25.</span><span class="name">Yum Woon Sen <span class="price">9.49</span><span class="desc">Ground chicken &amp; shrimp<br>with bean thread noodles,<br>celery &amp; onions</span></span></li>
  </ol>
</section>
<div class="photo" role="img" aria-label="Photo of spicy Thai beef salad with red onion on a white plate" style="left:620px;top:628px;width:152px;height:132px;background:radial-gradient(circle,#7a5a3e 0 35%,#8a6a4e 45%,#c98a9a 50%,#f5f3f0 58%,#fff 70%)"></div>

<section class="kids">
  <h2>Kids Menu</h2>
  <p>All kid's meals served with fries or rice (steamed or fried)<br>Chicken Nuggets (5) or Corn Dogs (1) 3.99 CN (9) CD (2) 4.99</p>
  <h3>Salad</h3>
  <p>*House Salad 4.29 with meal 2.89<br>Choice of dressing: Thai, Ranch, Italian,<br>Honey Mustard, Thousand Island</p>
</section>

<section class="section" style="left:808px;top:30px;width:384px;height:330px">
  <div class="ornament ornament--dark" role="img" aria-label="Illustration of a Thai mythical warrior figure" style="top:6px;width:46px;height:44px"></div>
  <h2 class="heading" style="position:absolute;top:56px;width:100%;font-size:22px">Thai Noodles</h2>
  <p class="sub" style="position:absolute;top:77px;width:100%;font-size:8.4px">Chicken, Pork, Tofu, Vegetarian 9.29<br>Beef 9.99 Shrimp or Squid 12.69 House 12.69</p>
  <ol class="menu" style="position:absolute;left:38px;top:100px;width:340px">
    <li class="item"><span class="num">27.</span><span class="name">Pad Kee Mow (Drunken Noodle)<span class="desc">Stir-fried with wide rice noodles, egg, vegetables, &amp; Thai Basil</span></span></li>
    <li class="item"><span class="num">28.</span><span class="name">Pad Thai<span class="desc">Thin rice noodles with bean sprouts, egg, stir-fried in sweet &amp;<br>sour sauce &amp; topped with ground peanuts<br>(Let your server know if you have an allergy to peanuts)</span></span></li>
    <li class="item"><span class="num">29.</span><span class="name">Mee Grob<span class="desc">Crispy egg noodles topped with<br>Chinese vegetables in gravy</span></span></li>
    <li class="item"><span class="num">30.</span><span class="name">Kway Teaw Lad Nar<span class="desc">Stir-fried with broccoli &amp; carrot<br>in a Thai soy sauce gravy over<br>a bed of wide rice noodles</span></span></li>
    <li class="item"><span class="num">31.</span><span class="name">Pad See Ew<span class="desc">Stir-Fried with egg,<br>broccoli, &amp; noodles</span></span></li>
    <li class="item"><span class="num">32.</span><span class="name">Lad Nar Ta Lay <span class="price">13.99</span><span class="desc">Shrimp, squid, rice noodles, broccoli &amp; Thai gravy</span></span></li>
  </ol>
  <div class="photo" role="img" aria-label="Photo of pad thai with lime and bean sprouts on a blue plate" style="left:244px;top:170px;width:116px;height:112px;background:radial-gradient(circle,#e0a060 0 30%,#f0d6a0 42%,#6d8ec2 52%,#4c6aa8 70%,#fff 71%)"></div>
</section>

<section class="section" style="left:808px;top:362px;width:384px;height:210px">
  <div class="ornament ornament--dark" role="img" aria-label="Illustration of a Thai mythical warrior figure" style="top:0;width:46px;height:40px"></div>
  <h2 class="heading" style="position:absolute;top:44px;width:100%;font-size:22px">Thai Noodles Soup</h2>
  <p class="sub" style="position:absolute;top:66px;width:100%">All salads tossed in our special spicy,<br>lemony dressing &amp; steam rice</p>
  <ol class="menu" style="position:absolute;left:38px;top:90px;width:340px">
    <li class="item"><span class="num">33.</span><span class="name">Beef Noodle Soup <span class="price">8.99</span><span class="desc">Beef with rice noodles, bean sprouts, &amp; green onion</span></span></li>
    <li class="item"><span class="num">34.</span><span class="name">Pork Noodle Soup <span class="price">7.99</span><span class="desc">Pork with rice noodles, bean sprouts, green onion, &amp; cilantro</span></span></li>
    <li class="item"><span class="num">35.</span><span class="name">Roast Pork Noodle Soup <span class="price">7.99</span><span class="desc">Roast pork with rice noodles, bean sprouts,<br>green onion, &amp; cilantro</span></span></li>
    <li class="item"><span class="num">36.</span><span class="name">Wonton Soup <span class="price">7.99</span><span class="desc">Thai Style with roast pork</span></span></li>
  </ol>
</section>

<section class="panel panel--plum" style="left:810px;top:582px;width:386px;height:300px">
  <div class="ornament ornament--light" role="img" aria-label="Illustration of a Thai mythical warrior figure" style="top:8px;width:46px;height:40px"></div>
  <h2 class="heading" style="position:absolute;top:50px;width:100%;font-size:22px">Thai Curries</h2>
  <p class="sub" style="position:absolute;top:71px;width:100%;font-size:8.4px">Chicken, Pork, Tofu, Vegetarian 9.49<br>Beef 10.49 Shrimp or Squid 12.99 House 12.99</p>
  <ol class="menu menu--wide" style="position:absolute;left:34px;top:92px;width:346px">
    <li class="item"><span class="num">37.</span><span class="name">Gang Ped (Red Curry)<span class="desc">Thai spices blended with Red Curry paste &amp; rich coconut milk<br>with bamboo, &amp; topped with green &amp; red bell peppers, &amp;<br>Thai basil</span></span></li>
    <li class="item"><span class="num">38.</span><span class="name">Gang Khew Whan (Green Curry)<span class="desc">Thai spices blended with Green Curry paste &amp; rich coconut<br>milk with bamboo, &amp; topped with green &amp; red bell peppers,<br>&amp; Thai basil</span></span></li>
    <li class="item"><span class="num">38B.</span><span class="name">Gang Karee (Yellow Curry)<span class="desc">Thai spices blended with Yellow Curry paste &amp; rich coconut<br>milk with potatoes, carrots, &amp; onions</span></span></li>
    <li class="item"><span class="num">38B.</span><span class="name">Gang Karee (Yellow Curry)<span class="desc">Massaman, mildest of all curries, is creamy and blended with<br>potatoes, carrot, onion, &amp; peanut</span></span></li>
    <li class="item"><span class="num">39.</span><span class="name">Panang Curry<span class="desc">Sweet red curry blended in rich coconut milk</span></span></li>
  </ol>
</section>

</body>
</html>
```